Offshore Energy Projects Management Consultancy needs a business card design

Logo available. We provide teams to deliver engineering consultancy, project management and delivery teams mainly in the offshore renewables sector. The company is all about bringing the right people to a project to deliver the scope.

The business card will be used for all staff.

The business card should be quite simple, vibrant and uncluttered but convey experience, enthusiasm and integration.

Target Market(s)

Energy Project Developers and Tier 1 construction companies

Contact Information for Business Card

Logo should be on the back of the card. I'm happy for the designer to play with the colour of the logo and background colour.

Front of the card should convey all the must have information in a clear and professional manner but without being overly traditional.

Colors

Designer to choose colors to be used in the design.

Requirements
Must have
• Land Line Tel Number, Mobile Tel Number, Email, business address, web address.

```html
<!DOCTYPE html>
<html lang="en">
<head>
<meta charset="utf-8">
<title>Tidewell Project Partners – Business Card</title>
<link href="https://fonts.googleapis.com/css2?family=Exo+2:wght@500;600;700&family=Questrial&display=swap" rel="stylesheet">
<style>
  :root {
    --stage: #5f5f5f;
    --paper: #ffffff;
    --brand-blue: #1a6fbd;
    --brand-sky: #22a6e3;
    --ink: #3e4347;
    --rule: #6b6f73;
  }
  * { box-sizing: border-box; margin: 0; padding: 0; }
  html, body { width: 1200px; height: 675px; overflow: hidden; }
  body {
    background: var(--stage);
    position: relative;
    font-family: "Questrial", "Helvetica Neue", Arial, sans-serif;
  }
  .card {
    position: absolute;
    top: 178px;
    width: 560px;
    height: 320px;
    overflow: hidden;
  }
  .card--front { left: 20px; background: var(--paper); }
  .card--back {
    left: 620px;
    background: linear-gradient(100deg, var(--brand-blue) 0%, var(--brand-sky) 100%);
  }
  .card__band {
    position: absolute; left: 0; right: 0; bottom: 0; height: 6px;
    background: linear-gradient(90deg, var(--brand-blue), var(--brand-sky));
  }

  .wordmark {
    position: absolute;
    display: flex; align-items: center; gap: 8px;
    font-family: "Exo 2", Arial, sans-serif;
    font-weight: 700;
    text-transform: uppercase;
    line-height: 1.05;
  }
  .wordmark__dot { border-radius: 50%; flex: none; }
  .card--front .wordmark {
    left: 36px; top: 128px; width: 230px;
    color: var(--brand-blue); font-size: 19px;
  }
  .card--front .wordmark__dot { width: 26px; height: 26px; background: var(--brand-blue); }
  .card--back .wordmark {
    left: 0; right: 0; top: 118px; justify-content: center;
    color: #ffffff; font-size: 30px; gap: 14px;
  }
  .card--back .wordmark__dot { width: 40px; height: 40px; background: #ffffff; }

  .divider {
    position: absolute; left: 284px; top: 66px;
    width: 1.5px; height: 188px; background: var(--rule);
  }
  .contact { position: absolute; left: 305px; top: 72px; color: var(--ink); }
  .contact__name {
    font-family: "Exo 2", Arial, sans-serif;
    font-weight: 600; font-size: 20px; letter-spacing: 0.3px;
    color: var(--brand-blue); line-height: 1.1;
  }
  .contact__role { font-size: 13.5px; margin-top: 2px; }
  .contact__address { font-size: 13.5px; line-height: 16px; margin-top: 12px; font-style: normal; }
  .contact__lines { list-style: none; margin-top: 12px; font-size: 13.5px; }
  .contact__lines li { display: flex; align-items: center; gap: 9px; height: 17.5px; }
  .contact__lines svg { width: 12px; height: 12px; flex: none; }
</style>
</head>
<body>

<section class="card card--front" aria-label="Business card front">
  <div class="wordmark">
    <span class="wordmark__dot"></span>
    <span>Tidewell Project Partners</span>
  </div>

  <div class="divider"></div>

  <div class="contact">
    <p class="contact__name">DORIAN HALE</p>
    <p class="contact__role">Founder &amp; CEO</p>
    <address class="contact__address">
      Tidewell Project Partners<br>
      Quai des Lilas 22<br>
      1201 Genève
    </address>
    <ul class="contact__lines">
      <li>
        <svg viewBox="0 0 12 12" aria-hidden="true"><path fill="var(--brand-sky)" d="M1 4c0-1.5 2.2-2.5 5-2.5S11 2.5 11 4v1H8.5V3.8h-5V5H1zM3 6h6l1.5 4.5h-9z"/></svg>
        <span>+9 111 222 3333</span>
      </li>
      <li>
        <svg viewBox="0 0 12 12" aria-hidden="true"><rect x="3" y="0.8" width="6" height="10.4" rx="1.2" fill="none" stroke="var(--brand-sky)" stroke-width="1.3"/><circle cx="6" cy="9.3" r=".7" fill="var(--brand-sky)"/></svg>
        <span>+9 111 222 3333</span>
      </li>
      <li>
        <svg viewBox="0 0 12 12" aria-hidden="true"><rect x="1" y="2.5" width="10" height="7" fill="none" stroke="var(--brand-sky)" stroke-width="1.2"/><path d="M1 2.8 6 6.5l5-3.7" fill="none" stroke="var(--brand-sky)" stroke-width="1.2"/></svg>
        <span>info@tidewellpartners.com</span>
      </li>
      <li>
        <svg viewBox="0 0 12 12" aria-hidden="true"><g fill="none" stroke="var(--brand-sky)" stroke-width="1"><circle cx="6" cy="6" r="5"/><ellipse cx="6" cy="6" rx="2.2" ry="5"/><path d="M1 6h10M1.8 3.5h8.4M1.8 8.5h8.4"/></g></svg>
        <span>tidewellpartners.com</span>
      </li>
    </ul>
  </div>

  <div class="card__band"></div>
</section>

<section class="card card--back" role="img" aria-label="Business card back: blue gradient field with a faint repeating brand pattern, company name centred">
  <div class="wordmark">
    <span class="wordmark__dot"></span>
    <span>Tidewell Project Partners</span>
  </div>
</section>

</body>
</html>
```